Riverbend City (by the numbers)

We (city communications office of Riverbend City, Arkansas) are launching a magazine to be delivered to every house in the community. We would like the first inside page to be an infographic of the important and interesting "numbers" from 2017. We want it to be visually interesting and convey the huge amount of important services we provide our residents. I have included a document with the relevant statistics to be used.

Target Market(s)

Residents of our city

Industry/Entity Type

House

Colors

Designer to choose colors to be used in the design.

Requirements
Must have
• Our logo must be prominent. The dimensions should be able to fit onto a standard full page magazine. If the infographic is best displayed on two pages we will accept that as well, and change our layout.
Nice to have
• Not every statistic we have provided must be used but if they can be, that is preferable. I have also included some inspirational infographics that appealed to me and inspired the idea, but I am excited about new concepts that might not look anything like those that I have provided.
Should not have
• The design should not have anything incorporated that cannot be presented to families in our community. It must be all ages friendly.

```html
<!DOCTYPE html>
<html lang="en">
<head>
<meta charset="utf-8">
<title>Riverbend City 2017 by the Numbers</title>
<link href="https://fonts.googleapis.com/css2?family=Montserrat:wght@500;700&family=Oswald:wght@500;700&family=Roboto+Condensed:wght@700&display=swap" rel="stylesheet">
<style>
:root{
  --navy:#0f2f6e;
  --slate:#4a5f78;
  --paper:#eef0ee;
  --purple:#a05fd0;
  --purple-dark:#6e3f97;
  --green:#6ab34a;
  --green-dark:#4d8a33;
  --green-light:#8cc63f;
  --teal:#3f8f73;
  --orange:#e07a35;
  --charcoal:#3b3b3b;
  --grey:#5a5a5a;
  --red:#e0161b;
  --brown:#5e4a3c;
  --rose:#d9646a;
  --sky:#3aa6d9;
  --white:#ffffff;
}
*{margin:0;padding:0;box-sizing:border-box}
html,body{width:926px;height:1200px;overflow:hidden;background:var(--paper)}
.page{position:relative;width:926px;height:1200px;background:var(--paper);font-family:"Roboto Condensed",sans-serif;font-weight:700;overflow:hidden}
.abs{position:absolute}
.edge{left:0;width:926px;background:var(--navy)}
.edge-top{top:0;height:20px}
.edge-bottom{top:1172px;height:28px}
.city-scene{left:0;top:700px;width:926px;height:472px;background:linear-gradient(180deg,rgba(238,240,238,0) 0%,rgba(214,216,212,.9) 40%,rgba(196,190,182,.9) 100%)}

.header-back{left:155px;top:50px;width:615px;height:216px;background:var(--slate)}
.header-band{left:0;top:70px;width:926px;height:176px;background:var(--navy)}
.brand{left:228px;top:140px;display:flex;align-items:center;gap:10px;color:var(--white);font-family:"Montserrat",sans-serif;font-weight:700;font-size:20px;letter-spacing:.5px;line-height:1.1}
.brand-mark{flex:none;width:36px;height:36px;border-radius:50%;background:var(--white)}
.year{left:398px;top:92px;color:var(--white);font-family:"Montserrat",sans-serif;font-weight:700;font-size:100px;line-height:1;letter-spacing:-1px}
.year-sub{left:402px;top:184px;color:var(--white);font-family:"Montserrat",sans-serif;font-weight:500;font-size:24px}

.pop-shadow{left:0;top:318px;width:440px;height:38px;background:var(--purple-dark)}
.pop-bar{left:0;top:308px;width:430px;height:44px;background:var(--purple);display:flex;align-items:center;color:var(--white);font-size:21px;letter-spacing:1px}
.pop-bar .label{margin-left:58px;width:188px}
.pop-bar .chev{width:84px;letter-spacing:-3px;color:#e6d2f5}
.pop-bar .value{margin-left:0}
.people-men{left:58px;top:378px;width:164px;height:124px;border-radius:6px;background:linear-gradient(180deg,rgba(63,143,115,.55),rgba(63,143,115,.35))}
.people-women{left:238px;top:378px;width:178px;height:124px;border-radius:6px;background:linear-gradient(180deg,rgba(224,122,53,.55),rgba(224,122,53,.35))}

.park-bar-shadow{left:560px;top:404px;width:366px;height:34px;background:var(--green-dark)}
.park-bar{left:540px;top:392px;width:386px;height:34px;background:var(--green);color:var(--white);font-size:20px;letter-spacing:1px}
.park-bar .chev{position:absolute;left:96px;top:5px;letter-spacing:-3px;color:#d9ecc9}
.park-bar .walkers{position:absolute;left:150px;top:9px;width:74px;height:16px;border-radius:8px;background:rgba(255,255,255,.45)}
.park-bar .value{position:absolute;left:240px;top:5px}
.park-title{left:640px;top:366px;color:var(--green);font-size:15.5px;letter-spacing:.6px}
.park-ring{left:456px;top:314px;width:150px;height:150px;border-radius:50%;background:var(--green)}
.park-icon{left:484px;top:342px;width:94px;height:94px;border-radius:50%;background:radial-gradient(circle at 50% 50%,#7fbf5c 0%,#9ccf80 38%,#ffffff 40%)}

.dots{height:0;border-top:4px dotted var(--navy)}
.dots-1{left:45px;top:518px;width:835px}
.dots-2{left:45px;top:724px;width:835px}
.dots-3{left:45px;top:898px;width:835px}
.dots-v{left:462px;top:910px;width:0;height:250px;border-left:4px dotted var(--navy)}

.road{left:0;top:664px;width:650px;height:26px;background:var(--charcoal)}
.road-shadow{left:0;top:690px;width:645px;height:16px;background:#8a8a8a}
.tag{background:var(--charcoal);color:var(--white);font-size:16px;letter-spacing:.5px;display:flex;align-items:center;justify-content:center;border-radius:4px}
.tag-police{left:128px;top:572px;width:118px;height:28px}
.tag-fire{left:402px;top:572px;width:118px;height:28px}
.num{background:var(--charcoal);color:var(--white);font-size:22px;display:flex;align-items:center;justify-content:center;border-radius:4px}
.num-police{left:148px;top:614px;width:98px;height:32px}
.num-fire{left:402px;top:614px;width:98px;height:32px}
.call-box{left:245px;top:553px;width:157px;height:110px;background:var(--red);border-radius:10px;display:flex;align-items:center;justify-content:center;gap:6px;color:var(--white);font-family:"Oswald",sans-serif;font-weight:700;font-size:58px}
.police-car{left:25px;top:616px;width:118px;height:46px;border-radius:22px 26px 8px 8px;background:linear-gradient(180deg,#4a4a4a,#262626)}
.fire-truck{left:508px;top:584px;width:108px;height:78px;border-radius:4px 14px 6px 6px;background:linear-gradient(180deg,#555,#2e2e2e)}

.lane{left:668px;top:540px;width:46px;height:165px;background:var(--charcoal)}
.lane-dash{left:688px;width:6px;height:20px;background:var(--white)}
.asphalt-num{left:728px;top:537px;color:var(--grey);font-family:"Oswald",sans-serif;font-weight:700;font-size:70px;line-height:1}
.asphalt-txt{left:731px;top:622px;color:var(--grey);font-size:18px;line-height:1.2;letter-spacing:1px}

.band{left:0;top:766px;width:926px;height:112px;background:var(--navy)}
.stat{top:745px;height:134px;color:var(--white)}
.stat-garbage{left:53px;width:255px;background:var(--purple)}
.stat-tires{left:331px;width:256px;background:var(--charcoal)}
.stat-yard{left:617px;width:256px;background:var(--green-light)}
.stat .big{position:absolute;font-family:"Oswald",sans-serif;font-weight:700;font-size:38px;line-height:1}
.stat .small{position:absolute;font-size:11.5px;line-height:1.2;letter-spacing:.3px;text-align:center}
.icon-fill{position:absolute;background:rgba(255,255,255,.35);border-radius:6px}

.parks-num{left:62px;top:912px;color:var(--brown);font-family:"Oswald",sans-serif;font-weight:700;font-size:190px;line-height:1;letter-spacing:-4px}
.parks-art{left:272px;top:950px;width:168px;height:135px;background:linear-gradient(180deg,#f3e66a 0%,#a9d67a 45%,#6ab34a 100%);border-radius:84px 84px 10px 10px;opacity:.85}
.parks-label{left:74px;top:1097px;color:var(--brown);font-family:"Oswald",sans-serif;font-weight:500;font-size:20px;letter-spacing:9.5px}

.heart{left:484px;top:908px}
.one{left:648px;top:955px;color:var(--sky);font-family:"Oswald",sans-serif;font-weight:700;font-size:86px;line-height:1}
.play-title{left:686px;top:960px;color:var(--rose);font-family:"Oswald",sans-serif;font-weight:700;font-size:34px;line-height:1.02}
.play-txt{left:656px;top:1045px;width:232px;color:var(--charcoal);font-size:16px;line-height:1.18;text-align:center;letter-spacing:.3px}
</style>
</head>
<body>
<main class="page">
  <div class="abs edge edge-top"></div>
  <div class="abs city-scene" role="img" aria-label="Faded aerial view of the city ballpark and downtown at dusk"></div>

  <header>
    <div class="abs header-back"></div>
    <div class="abs header-band"></div>
    <div class="abs brand"><span class="brand-mark"></span><span>RIVERBEND<br>CITY</span></div>
    <h1 class="abs year">2017</h1>
    <p class="abs year-sub">by the Numbers</p>
  </header>

  <section class="population">
    <div class="abs pop-shadow"></div>
    <div class="abs pop-bar"><span class="label">POPULATION</span><span class="chev">❯❯❯</span><span class="value">65,004</span></div>
    <div class="abs people-men" role="img" aria-label="Three rows of green male figure pictograms"></div>
    <div class="abs people-women" role="img" aria-label="Three rows of orange female figure pictograms"></div>
  </section>

  <section class="park-visitors">
    <div class="abs park-bar-shadow"></div>
    <div class="abs park-bar"><span class="chev">❮❮❮</span><span class="walkers" role="img" aria-label="Walking people pictograms"></span><span class="value">779,621</span></div>
    <div class="abs park-title">VISITORS TO MAPLE HOLLOW PARK</div>
    <div class="abs park-ring"></div>
    <div class="abs park-icon" role="img" aria-label="Tree and winding path park icon"></div>
  </section>

  <div class="abs dots dots-1"></div>

  <section class="emergency">
    <div class="abs road-shadow"></div>
    <div class="abs road"></div>
    <div class="abs police-car" role="img" aria-label="Police car illustration"></div>
    <div class="abs fire-truck" role="img" aria-label="Fire truck with ladder illustration"></div>
    <div class="abs tag tag-police">POLICE CALLS</div>
    <div class="abs num num-police">26,660</div>
    <div class="abs call-box">
      <svg width="30" height="46" viewBox="0 0 30 46" aria-hidden="true"><path d="M20 3 L12 5 C4 9 3 18 3 23 C3 28 4 37 12 41 L20 43 L24 33 L17 30 C13 27 13 19 17 16 L24 13 Z" fill="none" stroke="#fff" stroke-width="3.5" stroke-linejoin="round"/></svg>
      <span>911</span>
    </div>
    <div class="abs tag tag-fire">FIRE CALLS</div>
    <div class="abs num num-fire">12,560</div>
  </section>

  <section class="asphalt">
    <div class="abs lane"></div>
    <div class="abs lane-dash" style="top:556px"></div>
    <div class="abs lane-dash" style="top:596px"></div>
    <div class="abs lane-dash" style="top:636px"></div>
    <div class="abs lane-dash" style="top:676px"></div>
    <div class="abs asphalt-num">5,952</div>
    <p class="abs asphalt-txt">TONS OF ASPHALT<br>USED IN REPAIRING<br>POTHOLES AND<br>STREET OVERLAY</p>
  </section>

  <div class="abs dots dots-2"></div>
  <div class="abs band"></div>

  <section class="services">
    <div class="abs stat stat-garbage">
      <div class="icon-fill" role="img" aria-label="House and trash can icon" style="left:15px;top:23px;width:92px;height:90px"></div>
      <div class="big" style="left:114px;top:33px">16,768</div>
      <p class="small" style="left:118px;top:79px">TONS OF HOUSEHOLD<br>GARBAGE COLLECTED</p>
    </div>
    <div class="abs stat stat-tires">
      <div class="big" style="left:78px;top:18px">4,221</div>
      <p class="small" style="left:60px;top:62px;width:136px">USED TIRES RECYCLED</p>
      <div class="icon-fill" role="img" aria-label="Row of tire illustrations" style="left:14px;top:86px;width:236px;height:38px;border-radius:19px"></div>
    </div>
    <div class="abs stat stat-yard">
      <div class="big" style="left:14px;top:36px">116,675</div>
      <p class="small" style="left:14px;top:82px">CUBIC YARDS OF GREEN<br>YARD WASTE COLLECTED</p>
      <div class="icon-fill" role="img" aria-label="Person mowing the lawn pictogram" style="left:162px;top:26px;width:84px;height:86px"></div>
    </div>
  </section>

  <div class="abs dots dots-3"></div>
  <div class="abs dots-v"></div>

  <section class="parks">
    <div class="abs parks-num">34</div>
    <div class="abs parks-art" role="img" aria-label="Park illustration with sun, trees, hill and picnic table"></div>
    <div class="abs parks-label">NEIGHBORHOOD PARKS</div>
  </section>

  <section class="playground">
    <svg class="abs heart" width="164" height="210" viewBox="0 0 164 210" role="img" aria-label="Heart with children on a swing set">
      <path d="M82 200 C40 160 6 120 6 70 C6 32 30 8 58 8 C70 8 78 14 82 22 C86 14 96 8 108 8 C136 8 158 32 158 70 C158 120 124 160 82 200 Z" fill="#d9646a" stroke="#3aa6d9" stroke-width="6" stroke-linejoin="round"/>
    </svg>
    <div class="abs one">1</div>
    <h2 class="abs play-title">OPEN ARMS<br>PLAYGROUND</h2>
    <p class="abs play-txt">INCLUSIVE PLAYGROUNDS<br>BUILT FOR KIDS WITH<br>SPECIAL NEEDS</p>
  </section>

  <div class="abs edge edge-bottom"></div>
</main>
</body>
</html>
```